Rebrand our dated accomodation business website "Tallowind Quay Residences"

we have a wordpress website ( www.tallowindquay.com.au) that is old and out dated .
I will need a new updated SQUARESPACE website (in which i already have ) with a fresh new design , also new logo and an easy site to manage from my end.
Need to connect our socials - facebook and instagram and our new site
Check out "brindle cove landing" for inspiration...
These apartments are consists of -
-One bedroom One bath
-Two bedroom One bath
-Two bedroom Two bath
-Three bedroom Two bath
all other information is on our current website
KEEP it simple and fresh
ALSO WE DONT HAVE HUGE BIG BOATS IN THE MARINA SO PLEASE DONT HAVE THAT IN THE LOGO

Target Market(s)

Anyone looking for accomodation !! we have 64 rooms !!

Industry/Entity Type

accomodation / short stays

Coding

Coded - Design and coding required

Number of Pages Required

5+ page

Requirements
Must have
• Fresh , modern and easy to use.....have a hoilday vibe , also use natural colours
Nice to have
• i like accomodation website like ....https://fernandgrove.com.au/luxury-coastal-accommodation/ or https://theorvellainn.com/
Should not have
• please do not use bright colours and scripted fonts

```html
<!DOCTYPE html>
<html lang="en">
<head>
<meta charset="utf-8">
<title>Tallowind Quay Residences</title>
<link href="https://fonts.googleapis.com/css2?family=Manrope:wght@400;500;600;700&display=swap" rel="stylesheet">
<style>
:root{
  --bronze:#b48f66;
  --teal:#a7d0cf;
  --teal-deep:#9cc6c6;
  --mint:#eef8f7;
  --ink:#1f2326;
  --body:#3a3f42;
  --muted:#8a9396;
  --brand:#2c7aa1;
  --white:#ffffff;
  --line:#d7e4e3;
}
*{box-sizing:border-box;margin:0;padding:0}
html,body{width:1200px;height:4339px;overflow:hidden}
body{position:relative;font-family:"Manrope",Arial,sans-serif;color:var(--ink);background:var(--white)}
.abs{position:absolute}
.btn{position:absolute;display:flex;align-items:center;justify-content:center;font-size:14px;font-weight:600;text-transform:uppercase;letter-spacing:.2px}
.btn--solid{background:var(--bronze);color:var(--white)}
.btn--ghost{background:var(--white);color:var(--bronze);box-shadow:0 2px 8px rgba(0,0,0,.08)}
.section-title{position:absolute;left:0;width:1200px;text-align:center;font-size:40px;font-weight:500;text-transform:uppercase;letter-spacing:.5px}
.title-rule{position:absolute;left:553px;width:94px;height:2px;background:var(--teal)}
.photo{position:absolute}

/* header */
.topline{left:0;top:0;width:1200px;height:5px;background:var(--teal)}
.brand{display:flex;align-items:center;gap:10px;font-size:26px;font-weight:600;color:var(--brand);letter-spacing:.3px}
.brand__mark{width:14px;height:14px;background:var(--brand)}
.header__phone{left:673px;top:36px;font-size:17px;color:var(--teal-deep);display:flex;align-items:center;gap:8px;font-weight:500}
.social{width:32px;height:32px;background:#f1efe9;display:flex;align-items:center;justify-content:center}
.social span{width:10px;height:10px;border:2px solid var(--bronze);border-radius:2px}
.nav{left:452px;top:91px;display:flex;gap:30px;font-size:14px;font-weight:600;text-transform:uppercase}
.nav a{color:var(--ink);text-decoration:none}
.nav a.is-active{color:var(--bronze)}

/* hero */
.hero{left:0;top:132px;width:1200px;height:663px;overflow:hidden}
.hero__photo{left:0;top:0;width:1200px;height:663px;background:linear-gradient(180deg,#a9cde9 0%,#cfe3f0 33%,#2f6f93 40%,#2b6486 56%,#5f7c58 64%,#8e9a79 78%,#7c8561 100%)}
.hero__title{left:0;top:128px;width:1200px;text-align:center;font-size:44px;line-height:52px;font-weight:500;text-transform:uppercase;color:var(--ink)}
.dots{left:565px;top:514px;display:flex;gap:14px}
.dots span{width:13px;height:13px;background:rgba(255,255,255,.45)}
.dots span.on{background:var(--white)}
.scroll{left:1130px;top:395px;writing-mode:vertical-rl;color:var(--white);font-size:15px;letter-spacing:3px;font-weight:500}
.scroll-line{left:1143px;top:565px;width:1px;height:80px;background:rgba(255,255,255,.7)}
.scroll-btn{left:1128px;top:636px;width:32px;height:32px;border-radius:50%;background:var(--bronze);display:flex;align-items:center;justify-content:center}

/* about */
.about__ghost{left:-6px;top:990px;writing-mode:vertical-rl;transform:rotate(180deg);font-size:64px;font-weight:700;color:#f1f4f5;letter-spacing:2px}
.about__title{left:110px;top:985px;font-size:36px;line-height:45px;font-weight:500;text-transform:uppercase}
.about__text{left:110px;top:1112px;width:395px;font-size:15px;line-height:25.8px;color:var(--body);text-align:justify}

/* accommodations */
.accom{left:0;top:1555px;width:1200px;height:838px;background:var(--mint)}
.card{position:absolute;top:186px;width:300px}
.card__img{width:300px;height:342px}
.card__title{margin-top:27px;font-size:18px;font-weight:600;text-transform:uppercase}
.card__desc{margin-top:12px;font-size:14px;line-height:23px;color:var(--body)}
.card .btn{position:relative;margin-top:21px;width:142px;height:45px}
.arrow-box{width:38px;height:38px;display:flex;align-items:center;justify-content:center}

/* feedback */
.feedback{left:0;top:2393px;width:1200px;height:544px;background:linear-gradient(135deg,#a9d1d0,#97c3c3 60%,#a6cfcf)}
.quote-card{left:293px;top:170px;width:713px;height:297px;background:var(--white)}
.avatar-ring{left:193px;top:217px;width:204px;height:204px;border-radius:50%;background:var(--white);box-shadow:0 6px 18px rgba(0,0,0,.12)}
.avatar{left:210px;top:234px;width:170px;height:170px;border-radius:50%;background:radial-gradient(circle at 50% 45%,#c9c2b6,#9a9a90)}
.quote-text{left:430px;top:210px;width:518px;font-size:15.5px;line-height:25.5px;color:var(--body);text-align:justify}
.quote-name{left:430px;top:378px;font-size:19px;font-weight:600}
.stars{left:430px;top:406px;display:flex;gap:3px}

/* area */
.area__text{left:150px;width:900px;text-align:center;font-size:15.5px;line-height:25.5px;color:var(--body)}

/* footer */
.footer{left:0;top:3975px;width:1200px;height:364px;background:var(--mint)}
.footer h4{position:absolute;font-size:17px;font-weight:600;text-transform:uppercase}
.flinks{left:384px;top:110px;font-size:14px;line-height:31px;color:var(--body);list-style:none}
.flinks li::before{content:"»";color:var(--teal-deep);margin-right:12px}
.contact-row{position:absolute;left:533px;display:flex;gap:20px;font-size:14.5px;line-height:22px;color:var(--body)}
.icon-box{width:36px;height:36px;background:var(--white);display:flex;align-items:center;justify-content:center;flex:none}
</style>
</head>
<body>

<!-- Header -->
<div class="abs topline"></div>
<div class="abs brand" style="left:110px;top:44px"><span class="brand__mark"></span>Tallowind Quay Residences</div>
<div class="abs header__phone">
  <svg width="15" height="15" viewBox="0 0 24 24"><path d="M6.6 10.8a15 15 0 006.6 6.6l2.2-2.2c.3-.3.7-.4 1-.2 1.1.4 2.3.6 3.6.6.6 0 1 .4 1 1V20c0 .6-.4 1-1 1A17 17 0 013 4c0-.6.4-1 1-1h3.5c.6 0 1 .4 1 1 0 1.3.2 2.5.6 3.6.1.3 0 .7-.2 1z" fill="#9cc6c6"/></svg>
  1800 246 913
</div>
<div class="abs social" style="left:847px;top:32px"><span></span></div>
<div class="abs social" style="left:889px;top:32px"><span></span></div>
<div class="btn btn--solid" style="left:959px;top:25px;width:130px;height:47px">Book Now</div>
<nav class="abs nav">
  <a class="is-active">Home</a><a>About Us</a><a>Accommodation</a><a>Our Location</a><a>News</a><a>Contact Us</a>
</nav>

<!-- Hero -->
<section class="abs hero">
  <div class="abs hero__photo" role="img" aria-label="Aerial view of the jetty precinct, marina and headland island over a blue sea"></div>
  <svg class="abs" style="left:0;top:0" width="1200" height="663">
    <polygon points="0,520 410,590 0,663" fill="#a7d0cf"/>
    <polygon points="110,532 410,590 110,556" fill="#ffffff"/>
    <polygon points="410,590 1200,530 1200,663 0,663" fill="#ffffff"/>
  </svg>
  <h1 class="abs hero__title">Contemporary self contained<br>apartments Tallowind Bay<br>jetty precinct</h1>
  <div class="btn btn--solid" style="left:529px;top:298px;width:142px;height:46px">Get Started</div>
  <div class="abs dots"><span></span><span class="on"></span><span></span></div>
  <div class="abs scroll">SCROLL DOWN</div>
  <div class="abs scroll-line"></div>
  <div class="abs scroll-btn"><svg width="14" height="14" viewBox="0 0 14 14"><path d="M2 5l5 5 5-5" stroke="#fff" stroke-width="1.6" fill="none"/></svg></div>
</section>

<!-- About -->
<div class="abs about__ghost">ABOUT US</div>
<h2 class="abs about__title">About Tallowind Quay<br>Residences.</h2>
<p class="abs about__text">Tallowind Quay Residences is a modern accommodation complex situated in the heart of Tallowind Bay's vibrant Jetty precinct. The complex comprises 64 fully self-contained, privately owned apartments spread across three stories. Guests can choose from spacious 1, 2, or 3-bedroom apartments, each featuring modern decor, full kitchens, air-conditioned living areas, and private balconies or patios. Amenities include free Wi-Fi, Streamline TV, secure undercover parking, and direct lift access to all apartments</p>
<div class="btn btn--solid" style="left:110px;top:1403px;width:143px;height:44px">Learn More</div>
<div class="photo" style="left:711px;top:886px;width:489px;height:668px;background:linear-gradient(160deg,#e9eef0,#c9ccc8 45%,#6d706f 75%,#a59c8c)" role="img" aria-label="Bright open-plan living room with grey sofas and dining table by the balcony"></div>
<div class="photo" style="left:571px;top:1058px;width:283px;height:325px;background:#fff"></div>
<div class="photo" style="left:575px;top:1062px;width:275px;height:317px;background:linear-gradient(180deg,#5d8fc4,#b9d0de 40%,#e9ebea 60%,#b8bcbc)" role="img" aria-label="White outdoor shower beside a garden pathway under palms"></div>

<!-- Accommodations -->
<section class="abs accom">
  <h2 class="section-title" style="top:88px">Our Accommodations</h2>
  <div class="title-rule" style="top:138px"></div>
  <div class="abs arrow-box" style="left:38px;top:338px;background:#fff"><svg width="12" height="12" viewBox="0 0 12 12"><path d="M8 1L3 6l5 5" stroke="#b48f66" stroke-width="2" fill="none"/></svg></div>
  <div class="abs arrow-box" style="left:1124px;top:338px;background:var(--bronze)"><svg width="12" height="12" viewBox="0 0 12 12"><path d="M4 1l5 5-5 5" stroke="#fff" stroke-width="2" fill="none"/></svg></div>
  <article class="card" style="left:110px">
    <div class="card__img" style="background:linear-gradient(180deg,#f1f2f1,#d8d6d0 50%,#8a6a45)" role="img" aria-label="One bedroom apartment living and dining area with timber table"></div>
    <h3 class="card__title">One Bedroom One Bath</h3>
    <p class="card__desc">These comfortable, modern, and stylish apartments feature a Queen or King-size bed, an ensuite bathroom, a fully equipped kitchen...</p>
    <div class="btn btn--ghost">Book Now</div>
  </article>
  <article class="card" style="left:450px">
    <div class="card__img" style="background:linear-gradient(180deg,#eef0ef,#dfe1e0 55%,#2a3554 80%,#e9ebec)" role="img" aria-label="Twin bedroom with navy and white bedding"></div>
    <h3 class="card__title">Two Bedroom One Bath</h3>
    <p class="card__desc">These comfortable, modern, and stylish apartments feature a Queen or King-size bed, two single beds, both a main bathroom and an ensuite...</p>
    <div class="btn btn--solid">Book Now</div>
  </article>
  <article class="card" style="left:789px">
    <div class="card__img" style="background:linear-gradient(180deg,#f3f4f3,#c7cdc4 45%,#4f5250 75%,#9e9f9c)" role="img" aria-label="Three bedroom apartment dining setting opening to a garden patio"></div>
    <h3 class="card__title">Three Bedroom Two Bath</h3>
    <p class="card__desc">These comfortable, modern, and stylish apartments feature two Queen or King-size beds, two single beds, both a main bathroom and an ensuite...</p>
    <div class="btn btn--ghost">Book Now</div>
  </article>
</section>

<!-- Guest feedback -->
<section class="abs feedback">
  <h2 class="section-title" style="top:68px;color:#fff">Guest Feedback</h2>
  <div class="title-rule" style="top:118px;background:#fff"></div>
  <svg class="abs" style="left:82px;top:302px" width="48" height="24" viewBox="0 0 48 24"><path d="M46 12H3M13 2L2 12l11 10" stroke="#fff" stroke-width="2.5" fill="none"/></svg>
  <svg class="abs" style="left:1070px;top:302px" width="48" height="24" viewBox="0 0 48 24"><path d="M2 12h43M35 2l11 10-11 10" stroke="#fff" stroke-width="2.5" fill="none"/></svg>
  <div class="abs quote-card"></div>
  <div class="abs avatar-ring"></div>
  <div class="abs avatar" role="img" aria-label="Guest portrait"></div>
  <p class="abs quote-text">Our group of 5 senior adults stayed here for 1 night. The receptionist was friendly, helpful, polite &amp; full of information. The apartment was clean &amp; beautifully presented. There was more than sufficient kitchen items for our needs. The complex was within easy walking distance tobeach, shops &amp; restaurants. The road noise out front &amp; train noise out back didn't disturb our sleep.</p>
  <div class="abs quote-name">- MAREN T</div>
  <svg class="abs stars" width="86" height="14" viewBox="0 0 86 14">
    <g fill="#b48f66">
      <path id="st" d="M7 0l2 4.5 5 .5-3.8 3.3 1.1 4.9L7 10.7 2.7 13.2l1.1-4.9L0 5l5-.5z"/>
      <use href="#st" x="18"/><use href="#st" x="36"/><use href="#st" x="54"/><use href="#st" x="72"/>
    </g>
  </svg>
  <svg class="abs" style="left:898px;top:380px" width="50" height="40" viewBox="0 0 50 40"><g fill="#e1ecec"><path d="M0 40V20C0 8 6 2 18 0v8c-6 2-8 6-8 12h10v20z"/><path d="M26 40V20c0-12 6-18 18-20v8c-6 2-8 6-8 12h10v20z"/></g></svg>
</section>

<!-- Area -->
<h2 class="section-title" style="top:3045px">About Tallowind Bay</h2>
<div class="title-rule" style="top:3094px"></div>
<p class="abs area__text" style="top:3132px">Visitors to Tallowind Bay have the chance to explore a truly spectacular destination—where stunning beaches meet lush rainforests and scenic hinterland. A true vacation paradise, "Tallowind" offers something for everyone. Stay up to date with the latest attractions and events by checking our blog regularly.</p>
<p class="abs area__text" style="top:3224px">Tallowind Bay is also home to a world-class International Sports Stadium, hosting a wide range of exciting events throughout the year</p>
<svg class="abs" style="left:0;top:3360px" width="1200" height="400">
  <path d="M590 15H784V62" stroke="#b48f66" stroke-width="4" fill="none"/>
  <path d="M350 340V375H480" stroke="#b48f66" stroke-width="4" fill="none"/>
</svg>
<div class="photo" style="left:120px;top:3315px;width:463px;height:345px;background:linear-gradient(180deg,#7aa7cf,#c4d6e0 35%,#6f8b8e 55%,#8b8379 80%,#6e5a44)" role="img" aria-label="Runner on the marina breakwall path beside moored yachts"></div>
<div class="photo" style="left:489px;top:3432px;width:591px;height:351px;clip-path:polygon(101px 0,591px 0,591px 351px,0 351px,0 228px,101px 228px);background:linear-gradient(180deg,#c9bfd7,#e7d6df 40%,#b8b3bf 60%,#ece7e8)" role="img" aria-label="Father and son fishing in the shallows at dusk"></div>
<div class="btn btn--solid" style="left:529px;top:3835px;width:142px;height:45px">Learn More</div>

<!-- Footer -->
<footer class="abs footer">
  <div class="abs brand" style="left:110px;top:152px;font-size:22px"><span class="brand__mark" style="width:12px;height:12px"></span>Tallowind Quay</div>
  <h4 style="left:384px;top:60px">Navigation</h4>
  <ul class="abs flinks">
    <li>Home</li><li>About Us</li><li>Accommodation</li><li>Our Location</li><li>News/Events</li><li>Contact Us</li>
  </ul>
  <h4 style="left:533px;top:60px">Contact Us</h4>
  <div class="contact-row" style="top:108px">
    <span class="icon-box"><svg width="12" height="14" viewBox="0 0 12 14"><path d="M6 0a5 5 0 015 5c0 4-5 9-5 9S1 9 1 5a5 5 0 015-5z" fill="#c8dcdc"/><circle cx="6" cy="5" r="1.8" fill="#fff"/></svg></span>
    <span>14 Quayside Parade<br>Tallowind Bay NSW 2456</span>
  </div>
  <div class="contact-row" style="top:168px;align-items:center">
    <span class="icon-box"><svg width="14" height="11" viewBox="0 0 14 11"><rect width="14" height="11" rx="1" fill="#c8dcdc"/><path d="M1 1l6 5 6-5" stroke="#fff" stroke-width="1.3" fill="none"/></svg></span>
    <span>sales@tallowindquay.com.au</span>
  </div>
  <div class="contact-row" style="top:225px;align-items:center">
    <span class="icon-box"><svg width="13" height="13" viewBox="0 0 24 24"><path d="M6.6 10.8a15 15 0 006.6 6.6l2.2-2.2c.3-.3.7-.4 1-.2 1.1.4 2.3.6 3.6.6.6 0 1 .4 1 1V20c0 .6-.4 1-1 1A17 17 0 013 4c0-.6.4-1 1-1h3.5c.6 0 1 .4 1 1 0 1.3.2 2.5.6 3.6.1.3 0 .7-.2 1z" fill="#c8dcdc"/></svg></span>
    <span>1800 246 913</span>
  </div>
  <h4 style="left:809px;top:60px">Newsletter</h4>
  <div class="abs" style="left:809px;top:102px;font-size:13px;color:var(--body)">Email</div>
  <div class="abs" style="left:809px;top:133px;width:286px;height:1px;background:var(--line)"></div>
  <div class="btn btn--solid" style="left:809px;top:152px;width:131px;height:46px">Subscribe</div>
  <div class="abs" style="left:110px;top:305px;width:980px;height:1px;background:var(--line)"></div>
  <div class="abs" style="left:0;top:326px;width:1200px;text-align:center;font-size:13px;color:var(--body)">© 2026 &nbsp; | &nbsp; All Rights Reserved</div>
  <div class="abs" style="left:1012px;top:320px;width:32px;height:32px;background:var(--bronze);display:flex;align-items:center;justify-content:center"><span style="width:10px;height:10px;border:2px solid #fff;border-radius:2px"></span></div>
  <div class="abs social" style="left:1056px;top:320px;background:#fff"><span></span></div>
</footer>

</body>
</html>
```